International Freight Forwarder need a business card

We need a logo design for a freight forwarding company . We are active in Sea Transportation, Truck transportation, and Air Transportation, The design should be have normal dimensions of a card and should not have cuts and holes in its design (printed design is required - lamination accepted)

The said company is agent and sales representative of 2 other Shipping companies (whose logos, name, and website should also be mentioned on the card)

Industry/Entity Type

Logistics

Contact Information for Business Card

Address is "No.7, 2nd Darvish Kuche-ye-Sarvestani, Tehran, IR
Tel number is +98 21 66342819
Fax number is +98 21 66349527
E-Mail address is info@sarvnamavaran.com
Website is www.sarvnamavaran.com

Open Layer Logos attached as well

Colors
33a6d7
0292cd
0255a3
3276b5
85abd2
85cae6
cee9f5
d5e2ee
ffffff

Requirements
Must have
• Main logo of Sarvnama Varan
• Logo of KDR Shipping Line
• London, United Kingdom
• kdrline.com
• Logo of Coral Tide Shipping
• Dubai, United Arab Emirates
• ctsuae.com
• We require OPEN layer file to be submitted to us upon project selection.
Should not have
• Weird Designs such as cuts to the shape or holes in design.

```html
<!DOCTYPE html>
<html lang="en">
<head>
<meta charset="utf-8">
<title>Sarvnama Varan – Business Card</title>
<link href="https://fonts.googleapis.com/css2?family=Poppins:wght@400;500;600;700&display=swap" rel="stylesheet">
<style>
  :root {
    --navy: #1b4766;
    --navy-deep: #163a55;
    --navy-light: #245a7f;
    --brand-ink: #2b2a80;
    --ink: #1d3d5e;
    --muted: #9a9ea3;
    --ring: #d5d9de;
    --white: #ffffff;
    --stage: #e6eaee;
  }
  * { box-sizing: border-box; margin: 0; padding: 0; }
  html, body { width: 1200px; height: 900px; overflow: hidden; }
  body {
    background: var(--stage);
    font-family: "Poppins", sans-serif;
    position: relative;
  }
  .card {
    position: absolute;
    left: 240px;
    width: 720px;
    height: 410px;
    overflow: hidden;
    box-shadow: 0 10px 30px rgba(0,0,0,.18);
  }

  /* ---------- Back: partner lines ---------- */
  .card--back {
    top: 25px;
    background: radial-gradient(ellipse at 40% 40%, var(--navy-light), var(--navy-deep) 80%);
    color: var(--white);
  }
  .partner {
    position: absolute;
    display: flex;
    align-items: center;
    gap: 20px;
  }
  .partner--coral { left: 60px; top: 120px; }
  .partner--kdr { left: 390px; top: 150px; }
  .partner__mark {
    width: 96px; height: 96px;
    border: 5px solid var(--white);
    border-radius: 50%;
    flex: none;
  }
  .partner__text {
    text-align: center;
    line-height: 1.3;
    white-space: nowrap;
  }
  .partner__name { font-size: 18px; font-weight: 600; letter-spacing: .5px; }
  .partner__place, .partner__web { font-size: 15px; font-weight: 400; }
  .partner__name + .partner__place { margin-top: 6px; }

  /* ---------- Front: main card ---------- */
  .card--front {
    top: 465px;
    background: var(--white);
    color: var(--ink);
  }
  .brand {
    position: absolute;
    left: 40px; top: 34px;
    display: flex; align-items: center; gap: 22px;
  }
  .brand__ring {
    width: 120px; height: 120px;
    border: 3px solid var(--ring);
    border-radius: 50%;
  }
  .brand__name {
    color: var(--brand-ink);
    font-size: 19px;
    font-weight: 600;
    line-height: 1.3;
    text-align: center;
  }
  .divider {
    position: absolute;
    left: 40px; top: 190px;
    width: 400px; height: 2px;
    background: var(--ink);
  }
  .contacts {
    position: absolute;
    left: 40px; top: 212px;
    list-style: none;
    font-size: 17px;
    line-height: 28px;
  }
  .contacts li { display: flex; align-items: center; gap: 16px; }
  .contacts svg { width: 20px; height: 20px; fill: var(--ink); flex: none; }
  .person {
    position: absolute;
    right: 50px; top: 196px;
    text-align: right;
  }
  .person__name { font-size: 25px; font-weight: 500; letter-spacing: .5px; }
  .person__role { font-size: 17px; color: var(--muted); margin-top: 2px; }
  .address {
    position: absolute;
    right: 50px; top: 292px;
    text-align: right;
    font-size: 17px;
    line-height: 1.35;
  }
  .band {
    position: absolute;
    left: 0; bottom: 0;
    width: 720px; height: 56px;
  }
</style>
</head>
<body>

<section class="card card--back" aria-label="Card back with partner shipping lines">
  <div class="partner partner--coral">
    <div class="partner__mark"></div>
    <div class="partner__text">
      <p class="partner__name">CORAL TIDE<br>SHIPPING LLC</p>
      <p class="partner__place">Dubai, UAE</p>
      <p class="partner__web">www.ctsuae.com</p>
    </div>
  </div>
  <div class="partner partner--kdr">
    <div class="partner__mark"></div>
    <div class="partner__text">
      <p class="partner__name">KDR<br>Shipping Line Ltd</p>
      <p class="partner__place">London, UK</p>
      <p class="partner__web">www.kdrline.com</p>
    </div>
  </div>
</section>

<section class="card card--front" aria-label="Card front">
  <div class="brand">
    <div class="brand__ring"></div>
    <p class="brand__name">Sarvnama Varan<br>International<br>Transport.Co L.Lc</p>
  </div>

  <div class="divider"></div>

  <ul class="contacts">
    <li>
      <svg viewBox="0 0 24 24" aria-hidden="true"><path d="M3 9c0-3 4-5 9-5s9 2 9 5v2h-5V9H8v2H3zM6 12h12l2 8H4z"/></svg>
      +98 21 66342819
    </li>
    <li>
      <svg viewBox="0 0 24 24" aria-hidden="true"><path d="M7 3h10v6H7zM3 10h18v11H3zM6 13h3v2H6zm5 0h3v2h-3zm5 0h3v2h-3zM6 17h3v2H6zm5 0h3v2h-3zm5 0h3v2h-3z"/></svg>
      +98 21 66349527
    </li>
    <li>
      <svg viewBox="0 0 24 24" aria-hidden="true"><path d="M2 5h20v14H2zm2 2v.5l8 6 8-6V7zm0 3v7h16v-7l-8 6z"/></svg>
      info@sarvnamavaran.com
    </li>
    <li>
      <svg viewBox="0 0 24 24" aria-hidden="true"><path d="M14 2a8 8 0 1 1-5.3 14l-5.3 5.3-1.4-1.4L7.3 14.6A8 8 0 0 1 14 2zm0 2.5a5.5 5.5 0 1 0 0 11 5.5 5.5 0 0 0 0-11z"/></svg>
      www.sarvnamavaran.com
    </li>
  </ul>

  <div class="person">
    <p class="person__name">MS. SHIRIN TAVAKOLI</p>
    <p class="person__role">Chief Financial Officer</p>
  </div>

  <p class="address">No.7, 2nd Darvish<br>Kuche-ye-Sarvestani, Tehran, IR</p>

  <svg class="band" viewBox="0 0 720 56" preserveAspectRatio="none" aria-hidden="true">
    <path d="M0 6 H470" stroke="var(--navy)" stroke-width="2" fill="none"/>
    <path d="M0 14 H440 C470 14 470 24 500 24 H720 V56 H0 Z" fill="var(--navy)"/>
    <path d="M0 20 H445 C472 20 474 28 500 28 H720" stroke="var(--white)" stroke-width="3" fill="none"/>
  </svg>
</section>

</body>
</html>
```